professional business card design for technology company

We are a small technology consulting firm, specialising in consulting based around Cloud and Managed services. Our colour scheme is yellow, blue and white, as you can see in the logos. Although we are based in melbourne australia, due to the nature of our work, our clients can be located anywhere. We are looking for a clean, professional, positive look - similar to our company logo

Target Market(s)

small business

Industry/Entity Type

Business

Contact Information for Business Card

eye catching, designed to incorporate some level of raised printing. Must contain website address, phone number, name and job title

Requirements
Must have
• Logo (attached) - use of the same colour scheme

```html
<!DOCTYPE html>
<html lang="en">
<head>
<meta charset="utf-8">
<title>Solvara Business Card</title>
<link href="https://fonts.googleapis.com/css2?family=Lato:wght@400;700;900&display=swap" rel="stylesheet">
<style>
  :root {
    --backdrop: #1d1f1f;
    --card-white-top: #ffffff;
    --card-white-bottom: #dfe2e3;
    --charcoal: #454f4d;
    --charcoal-dark: #3e4846;
    --ink: #3a4141;
    --sky: #4cc4ee;
    --sun: #f5e100;
    --white: #ffffff;
  }
  * { margin: 0; padding: 0; box-sizing: border-box; }
  html, body {
    width: 1200px;
    height: 864px;
    overflow: hidden;
    background: var(--backdrop);
    font-family: "Lato", sans-serif;
  }
  .stage { position: relative; width: 1200px; height: 864px; }

  .card {
    position: absolute;
    left: 362px;
    width: 502px;
    height: 296px;
    overflow: hidden;
  }

  /* Front */
  .card-front {
    top: 103px;
    background: linear-gradient(160deg, var(--card-white-top) 35%, var(--card-white-bottom) 100%);
  }
  .card-front .accent-line {
    position: absolute;
    top: 0; left: 0;
    width: 240px; height: 2px;
    background: var(--sky);
    opacity: 0.5;
  }
  .card-front .brand-name {
    position: absolute;
    left: 60px;
    top: 128px;
    width: 150px;
    text-align: center;
    font-size: 26px;
    font-weight: 700;
    color: var(--sky);
    line-height: 1;
  }
  .contact {
    position: absolute;
    left: 223px;
    top: 77px;
    color: var(--ink);
  }
  .contact .person-name {
    font-size: 23px;
    font-weight: 400;
    line-height: 1.1;
  }
  .contact .job-title {
    font-size: 15px;
    color: var(--sky);
    line-height: 1.2;
  }
  .contact .details {
    list-style: none;
    margin-top: 22px;
    font-size: 15px;
    line-height: 22px;
  }
  .contact .label { color: var(--sky); }
  .address-band {
    position: absolute;
    left: 0; bottom: 0;
    width: 100%;
    height: 43px;
    background: var(--charcoal);
    color: var(--sun);
    font-size: 16px;
    line-height: 43px;
    text-align: center;
  }

  /* Back */
  .card-back {
    top: 457px;
    background: radial-gradient(circle at 35% 50%, #4a5553 0%, var(--charcoal-dark) 70%);
  }
  .card-back .wordmark {
    position: absolute;
    left: 0; top: 134px;
    width: 100%;
    display: flex;
    align-items: center;
    justify-content: center;
    gap: 14px;
  }
  .card-back .mark-dot {
    width: 26px; height: 26px;
    border-radius: 50%;
    background: var(--sky);
  }
  .card-back .brand-name {
    font-size: 40px;
    font-weight: 700;
    color: var(--white);
    line-height: 1;
  }
</style>
</head>
<body>
  <main class="stage">
    <section class="card card-front">
      <div class="accent-line"></div>
      <div class="brand-name">Solvara</div>
      <div class="contact">
        <div class="person-name">John Smith</div>
        <div class="job-title">Managing Director</div>
        <ul class="details">
          <li><span class="label">T:</span> 044-123 456 789</li>
          <li><span class="label">E:</span> info@webname.com</li>
          <li><span class="label">W:</span> www.websitename.com</li>
        </ul>
      </div>
      <div class="address-band">12345, Address Goes Here Country Name, 123456</div>
    </section>

    <section class="card card-back">
      <div class="wordmark">
        <span class="mark-dot"></span>
        <span class="brand-name">Solvara</span>
      </div>
    </section>
  </main>
</body>
</html>
```